Land Buying Company Needs Letterhead for Direct Mail Marketing to Land Owners

We are looking for a professional letterhead that we will be including in our direct mail marketing. We will be sending this to land owners who may be interested in selling or purchasing land.

The letterhead needs to be editable. Headers and footers would look nice, but we are open. We would want it to include our address, website, phone, and email info. For right now the address to use for design purposes would the following:

Address: 412 Fenwick Avenue #300
Dallas, TX 75319
Website - www.quillbrookacres.com
Email - info@quillbrookacres.com
Phone - 866-492-ACRE

I have attached our logo zip file that we just had done on Pixel Harbor. Let me know what questions you have, and thank you.

```html
<!DOCTYPE html>
<html lang="en">
<head>
<meta charset="utf-8">
<title>Quillbrook Acres Letterhead</title>
<link rel="stylesheet" href="https://fonts.googleapis.com/css2?family=Montserrat:wght@600&family=Arimo:wght@400&display=swap">
<style>
  :root {
    --backdrop: #e0e0e0;
    --paper: #ffffff;
    --paper-edge: #c9c9c9;
    --leaf: #97c23b;
    --forest: #3f5a1f;
    --ink: #555555;
    --faint: #f0f0f0;
    --rule-grey: #bdbdbd;
  }
  * { margin: 0; padding: 0; box-sizing: border-box; }
  html, body {
    width: 1200px; height: 1200px; overflow: hidden;
    background: var(--backdrop);
  }
  .letterhead {
    position: absolute; left: 175px; top: 50px;
    width: 850px; height: 1100px;
    background: var(--paper);
    border: 1px solid var(--paper-edge);
    overflow: hidden;
  }
  .letterhead__art { position: absolute; inset: 0; }
  .brand {
    position: absolute; left: 35px; top: 40px;
    display: flex; align-items: center; gap: 14px;
  }
  .brand__dot {
    width: 56px; height: 56px; border-radius: 50%;
    background: var(--forest);
  }
  .brand__name {
    font-family: "Montserrat", sans-serif; font-weight: 600;
    font-size: 30px; letter-spacing: 1px; color: var(--leaf);
  }
  .contact {
    position: absolute; left: 60px; top: 922px;
    list-style: none; width: 314px;
  }
  .contact__item {
    display: flex; align-items: center; height: 31.5px;
  }
  .contact__icon {
    width: 22px; height: 22px; border-radius: 4px;
    background: var(--forest); flex: none;
    display: flex; align-items: center; justify-content: center;
  }
  .contact__text {
    margin-left: 18px; flex: 1; height: 31.5px;
    display: flex; align-items: center; padding-left: 6px;
    font-family: "Arimo", sans-serif; font-size: 13.5px; color: var(--ink);
    border-bottom: 1.5px solid var(--leaf);
  }
  .contact__item:first-child .contact__text { border-bottom-color: var(--rule-grey); }
</style>
</head>
<body>
  <main class="letterhead">
    <svg class="letterhead__art" width="850" height="1100" viewBox="0 0 850 1100" aria-hidden="true">
      <circle cx="687" cy="840" r="300" fill="var(--faint)"/>
      <polygon points="447,0 850,0 850,99 519,99" fill="var(--leaf)"/>
      <polygon points="447,0 466,0 519,99 497,99" fill="var(--forest)"/>
    </svg>

    <header class="brand">
      <span class="brand__dot"></span>
      <span class="brand__name">QUILLBROOK ACRES</span>
    </header>

    <ul class="contact">
      <li class="contact__item">
        <span class="contact__icon">
          <svg width="12" height="14" viewBox="0 0 12 14"><path d="M6 0a5 5 0 0 0-5 5c0 4 5 9 5 9s5-5 5-9a5 5 0 0 0-5-5zm0 7a2 2 0 1 1 0-4 2 2 0 0 1 0 4z" fill="#fff"/></svg>
        </span>
        <span class="contact__text">412 Fenwick Avenue #300 Dallas, TX 75319</span>
      </li>
      <li class="contact__item">
        <span class="contact__icon">
          <svg width="13" height="13" viewBox="0 0 13 13"><path d="M3 0l2 3-1.3 1.5a8 8 0 0 0 4.8 4.8L10 8l3 2-1 2.5C6 13 0 7 .5 1z" fill="#fff"/></svg>
        </span>
        <span class="contact__text">866-492-ACRE</span>
      </li>
      <li class="contact__item">
        <span class="contact__icon">
          <svg width="13" height="10" viewBox="0 0 13 10"><rect x=".5" y=".5" width="12" height="9" fill="#fff"/><path d="M.5 .5l6 5 6-5" fill="none" stroke="var(--forest)" stroke-width="1.2"/></svg>
        </span>
        <span class="contact__text">info@quillbrookacres.com</span>
      </li>
      <li class="contact__item">
        <span class="contact__icon">
          <svg width="12" height="12" viewBox="0 0 12 12"><circle cx="6" cy="6" r="5.2" fill="none" stroke="#fff" stroke-width="1.3"/><path d="M1 6h10M6 1c-3 3-3 7 0 10M6 1c3 3 3 7 0 10" fill="none" stroke="#fff" stroke-width="1"/></svg>
        </span>
        <span class="contact__text">www.quillbrookacres.com</span>
      </li>
    </ul>
  </main>
</body>
</html>
```